Morrow & Pellant Stationery

Greetings again. Now we've got an awesome logo, it's time to get the stationery to go with it. We require the following items of stationery:

- Business Card - Print Ready, all we need to do is change names and numbers and submit to printer.  Double sided with logo on one side and details on the other side. (85mm x 55mm)

- With Compliments Slip

- Letterhead - These will be preprinted pages that will then be used as pages.
(A4)

- Envelope - Business Size(Standard DL)

Target Market(s)

Essentially, this firm services clients facing criminal charges and/or seeking legal aid. The firm is also looking at taking on more white-collar crime cases.

Requirements
Must have
• - Same Design Cues & Colours as the Branding details attached

• - Address (as follows)

• Suite 8

• 212-216 Carrow St

• KELLBROOK VIC 3990

• Phone: (03) 9555 0142

• Fax: (03) 9555 0187

• Web: www.morrowandpellant.example

• - Colour: Pantone 194 (Red)

```html
<!DOCTYPE html>
<html lang="en">
<head>
<meta charset="utf-8">
<title>Morrow &amp; Pellant – Business Card Concept 01</title>
<link rel="stylesheet" href="https://fonts.googleapis.com/css2?family=Cinzel:wght@400;600&family=Crimson+Text:wght@400&family=Arimo:wght@400&display=swap">
<style>
  :root {
    --brand-red: #a80638;
    --paper: #ffffff;
    --sheet: #ffffff;
    --meta-grey: #8a8a8a;
    --card-border: #8c8c8c;
    --divider-grey: #b5b5b5;
    --ink: #2a2a2a;
    --ghost: rgba(255, 255, 255, 0.12);
  }
  * { box-sizing: border-box; margin: 0; padding: 0; }
  html, body {
    width: 1200px; height: 946px; overflow: hidden;
    background: var(--sheet);
  }
  .sheet { position: relative; width: 1200px; height: 946px; }

  .sheet-meta {
    position: absolute; left: 16px; top: 4px;
    font: 400 12px/1 "Arimo", sans-serif; color: var(--meta-grey);
  }
  .sheet-meta .gap { display: inline-block; width: 22px; }
  .concept-number {
    position: absolute; left: 16px; top: 20px;
    font: 400 26px/1 "Arimo", sans-serif; color: var(--meta-grey);
  }

  .card { position: absolute; overflow: hidden; }
  .card--front-white { left: 16px; top: 94px; width: 552px; height: 364px;
    background: var(--paper); border: 2px solid var(--card-border); }
  .card--front-red { left: 612px; top: 94px; width: 556px; height: 364px;
    background: linear-gradient(to bottom,
      var(--brand-red) 0, var(--brand-red) 100px,
      #fff 170px, #fff 226px, var(--brand-red) 232px, var(--brand-red) 100%); }
  .card--back { top: 476px; width: 556px; height: 356px; background: var(--brand-red); }
  .card--back-left { left: 12px; }
  .card--back-right { left: 612px; }

  .lockup { position: absolute; display: flex; align-items: center; }
  .lockup__mark { width: 78px; height: 78px; border-radius: 50%; background: var(--brand-red); }
  .lockup__rule { width: 2px; height: 84px; background: var(--divider-grey); margin: 0 18px 0 20px; }
  .lockup__name {
    font: 600 27px/1 "Cinzel", serif; color: var(--ink); letter-spacing: 0.5px;
  }
  .lockup__tagline {
    margin-top: 6px;
    font: 400 14.5px/1 "Cinzel", serif; color: var(--ink); letter-spacing: 1.6px;
  }
  .card--front-white .lockup { left: 76px; top: 78px; }
  .card--front-red .lockup { left: 100px; top: 126px; }

  .contact {
    position: absolute; font-style: normal;
    font: 400 14px/17px "Crimson Text", serif;
  }
  .card--front-white .contact { color: var(--brand-red); }
  .contact--white-address { left: 200px; top: 206px; }
  .contact--white-numbers { left: 200px; top: 274px; }
  .card--front-red .contact { color: #fff; }
  .contact--red-address { left: 60px; top: 272px; }
  .contact--red-numbers { left: 264px; top: 272px; }

  .ghost-mark {
    position: absolute; width: 308px; height: 308px; border-radius: 50%;
    background: var(--ghost);
    display: flex; align-items: center; justify-content: center;
    font: 600 30px/1.1 "Cinzel", serif; color: var(--ghost); text-align: center;
  }
  .card--back-left .ghost-mark { left: 130px; top: 20px; }
  .card--back-right .ghost-mark { left: 128px; top: 20px; }
</style>
</head>
<body>
<main class="sheet">
  <p class="sheet-meta">format: ai / eps / cdr / pdf / psd / jpg / gif / png<span class="gap"></span>colors: RGB / CMYK / Pantone</p>
  <p class="concept-number">01*</p>

  <section class="card card--front-white" aria-label="Business card front, white">
    <div class="lockup">
      <div class="lockup__mark" aria-hidden="true"></div>
      <div class="lockup__rule" aria-hidden="true"></div>
      <div>
        <p class="lockup__name">Morrow &amp; Pellant</p>
        <p class="lockup__tagline">BARRISTERS &amp; SOLICITORS</p>
      </div>
    </div>
    <address class="contact contact--white-address">
      Suite 8<br>212-216 Carrow St<br>KELLBROOK VIC 3990
    </address>
    <p class="contact contact--white-numbers">
      Phone: (03) 9555 0142<br>Fax: (03) 9555 0187<br>Web: www.morrowandpellant.example
    </p>
  </section>

  <section class="card card--front-red" aria-label="Business card front, red">
    <div class="lockup">
      <div class="lockup__mark" aria-hidden="true"></div>
      <div class="lockup__rule" aria-hidden="true"></div>
      <div>
        <p class="lockup__name">Morrow &amp; Pellant</p>
        <p class="lockup__tagline">BARRISTERS &amp; SOLICITORS</p>
      </div>
    </div>
    <address class="contact contact--red-address">
      Suite 8<br>212-216 Carrow St<br>KELLBROOK VIC 3990
    </address>
    <p class="contact contact--red-numbers">
      Phone: (03) 9555 0142<br>Fax: (03) 9555 0187<br>Web: www.morrowandpellant.example
    </p>
  </section>

  <section class="card card--back card--back-left" aria-label="Business card back">
    <div class="ghost-mark">Morrow &amp;<br>Pellant</div>
  </section>

  <section class="card card--back card--back-right" aria-label="Business card back, alternate">
    <div class="ghost-mark">Morrow &amp;<br>Pellant</div>
  </section>
</main>
</body>
</html>
```